LANDING PAGE on a Word Press platform.

I have a website, www.thecalmledgermerchant.com and need to create a new landing page. I purchased a new url, www.calmledgermerchant.com and set it up on Word Press. It has a theme (I was trying to do it myself, but gave up) but you can change it if you need to. I will give you access so you can work directly on the Word Press Platform. Please visit my site, www.thecalmledgermerchant, so you can see what we are selling.
Updates

Thank you for being so patient. Unfortunately I had some pressing personal problems and had to leave the country for a couple of weeks. I am back now and will choose a design today. Thank you again!

Target Market(s)

Stock Market, High Worth Individuals, Traders, Investors

Requirements
Must have
• My landing page must look very professional and rich. I am sending a copy of my logo but the "the" before The Calm Ledger Merchant, needs to be removed. Some testimonials and services we provide. (all found on my home page)
Nice to have
• I am open to a new color scheme if possible. The logo colors would have to be changed.
Should not have
• Should not be too busy with too many images or text. I want a clean and easy to read landing page

```html
<!DOCTYPE html>
<html lang="en">
<head>
<meta charset="utf-8">
<title>Calm Ledger Merchant</title>
<link href="https://fonts.googleapis.com/css2?family=Raleway:wght@400;500;600;700&family=Arimo:wght@400;700&display=swap" rel="stylesheet">
<style>
:root{
  --navy:#1b1846;
  --gold:#b08a2e;
  --gold-soft:#c39a3a;
  --text:#6b6b6b;
  --dark:#222;
  --band:#f3f3f3;
  --rule:#dedede;
}
*{box-sizing:border-box;margin:0;padding:0}
html,body{width:726px;height:1200px;overflow:hidden;background:#fff}
body{position:relative;font-family:"Arimo",Arial,sans-serif;color:var(--text);font-size:6.4px;line-height:1.85}
.abs{position:absolute}
h1,h2,h3{font-family:"Raleway",Arial,sans-serif;color:var(--navy);font-weight:600}

.brand{left:60px;top:14px;display:flex;align-items:center;gap:6px}
.brand-mark{width:42px;height:42px;border-radius:50%;background:var(--navy)}
.brand-name{font-family:"Raleway",sans-serif;font-weight:700;font-size:15px;line-height:1.05;color:var(--navy)}

.auth{top:27px;height:21px;color:#fff;font-size:8px;font-family:"Raleway",sans-serif;font-weight:600;display:flex;align-items:center;justify-content:center;gap:4px}
.auth.login{left:552px;width:53px;background:var(--gold)}
.auth.logout{left:611px;width:55px;background:var(--navy)}

.nav{left:60px;top:70px;width:606px;height:32px;background:var(--navy);display:flex}
.nav a{color:#fff;text-decoration:none;font-size:7.6px;font-family:"Raleway",sans-serif;font-weight:500;display:flex;align-items:center;justify-content:center;border-right:1px solid #2d2a5c;flex:1}
.nav a.active{background:var(--gold);flex:0 0 64px}
.nav a:last-child{border-right:none}

.hero{left:60px;top:105px;width:606px;height:269px;background:radial-gradient(ellipse at 55% 55%,#2a7fd0 0%,#123a78 35%,#0a1424 75%)}
.hero-arrows{right:8px;bottom:8px;display:flex;gap:4px}

.welcome{left:60px;top:396px;width:606px;text-align:center}
.welcome h1{font-size:16px;font-weight:600;letter-spacing:.2px}
.welcome .sub{font-family:"Raleway",sans-serif;color:var(--gold);font-size:9.6px;margin-top:6px}
.welcome p{margin-top:6px;padding:0 44px;line-height:1.95}
.rule{left:60px;top:496px;width:606px;height:1px;background:var(--rule)}

.col{top:518px}
.col h2{font-size:12.5px;font-weight:600;margin-bottom:7px}
.col p{margin-bottom:6px}
.lead{color:var(--gold)}
.more{color:var(--gold);font-size:7px;font-weight:700}
.news-img{width:186px;height:85px;background:linear-gradient(135deg,#1a2a4a,#3a77b5 55%,#7aa6d4);border:3px solid #e6e6e6;position:relative}
.news-date{position:absolute;right:0;bottom:0;background:var(--gold);color:#fff;font-size:7px;padding:1px 6px}
.services li{list-style:none;display:flex;align-items:center;gap:8px;margin-bottom:1.5px}
.dot{width:6px;height:6px;border-radius:50%;border:1.5px solid var(--gold)}

.band{left:0;top:700px;width:726px;height:210px;background:var(--band);border-top:1px solid #e2e2e2;border-bottom:1px solid #e2e2e2}
.monitor{left:72px;top:708px;width:200px;height:188px;background:linear-gradient(180deg,#1d1d1d 0%,#3c3c3c 70%,#c9c9c9 100%);border-radius:4px}
.band-text{left:295px;top:716px;width:350px}
.band-text h2{font-size:12.5px;margin-bottom:9px}
.band-text p{margin-bottom:9px}
.subscribe{left:296px;top:854px;width:350px;height:25px;background:#fff;border:1px solid #e0e0e0;border-radius:13px;overflow:hidden}
.subscribe span{position:absolute;left:13px;top:7px;font-size:6px;color:#999}
.subscribe b{position:absolute;right:0;top:0;height:100%;width:93px;background:var(--navy);color:#fff;font-weight:400;font-size:7px;display:flex;align-items:center;justify-content:center;gap:6px;border-radius:0 13px 13px 0}

.report{left:60px;top:928px;width:606px;text-align:center}
.report h2{font-size:12.5px}
.report .sub{font-family:"Raleway",sans-serif;font-style:italic;color:var(--gold);font-size:8.4px;margin-top:4px}
.report p{margin-top:6px;padding:0 50px}
.pager{left:348px;top:1019px;display:flex;gap:4px}
.pager i{width:6px;height:6px;border-radius:50%;border:1px solid #333}
.pager i.on{border-color:var(--gold)}

.footer{left:0;top:1048px;width:726px;height:114px;background:var(--navy);color:#d8d8e6}
.footer h3{color:#fff;font-size:10px;font-weight:600;letter-spacing:.4px;margin-bottom:7px}
.fcol{top:16px}
.social{display:flex;gap:6px;margin-top:9px}
.social i{width:20px;height:20px;border-radius:50%;border:1.5px solid #fff}
.contact li{list-style:none;display:flex;gap:10px;align-items:center;margin-bottom:6px}
.news-form{width:180px;height:21px;background:#fff;border-radius:11px;position:relative;margin-top:6px}
.news-form span{position:absolute;left:10px;top:5px;font-size:6px;color:#888}
.news-form b{position:absolute;right:0;top:0;height:100%;width:55px;background:var(--gold);color:#fff;border-radius:11px;font-weight:400;font-size:7px;display:flex;align-items:center;justify-content:center}
.copy{left:0;top:1162px;width:726px;height:38px;background:var(--gold);color:#fff;font-size:6px;text-align:center;line-height:38px}
</style>
</head>
<body>

<header>
  <div class="abs brand">
    <div class="brand-mark"></div>
    <div class="brand-name">Calm Ledger<br>Merchant</div>
  </div>
  <a class="abs auth login"><svg width="7" height="7" viewBox="0 0 10 10"><circle cx="5" cy="3" r="2.4" fill="#fff"/><path d="M0.5 10a4.5 4 0 0 1 9 0z" fill="#fff"/></svg>LOGIN</a>
  <a class="abs auth logout"><svg width="7" height="7" viewBox="0 0 10 10"><rect x="1" y="4.5" width="8" height="5.5" fill="#fff"/><path d="M3 4.5V3a2 2 0 0 1 4 0v1.5" stroke="#fff" fill="none" stroke-width="1.3"/></svg>LOGOUT</a>
  <nav class="abs nav">
    <a class="active">HOME</a><a>ABOUT</a><a>CURRENT PORTFOLIO</a><a>LATEST REPORT</a><a>WATCH LIST</a><a>DAILY TICKER</a><a>MARKET NEWS</a>
  </nav>
</header>

<section class="abs hero" role="img" aria-label="Photo of a hand touching a glowing tablet with network icons and a rising market chart">
  <div class="abs hero-arrows">
    <svg width="16" height="16" viewBox="0 0 16 16"><circle cx="8" cy="8" r="7.5" fill="#d9d9d9"/><path d="M9.5 4.5 6 8l3.5 3.5" stroke="#333" stroke-width="1.6" fill="none"/></svg>
    <svg width="16" height="16" viewBox="0 0 16 16"><circle cx="8" cy="8" r="7.5" fill="#d9d9d9"/><path d="M6.5 4.5 10 8l-3.5 3.5" stroke="#333" stroke-width="1.6" fill="none"/></svg>
  </div>
</section>

<section class="abs welcome">
  <h1>WELCOME TO CALM LEDGER MERCHANT</h1>
  <div class="sub">Our Team of Researchers, Stock Traders and Contributors</div>
  <p>If you are an investor or stock trader looking for high quality investment ideas with strong fundamentals to support them, look no further than the "The Calm Ledger Merchant" as an invaluable resource of investment information. Our approach combines fundamental and technical analysis in order to introduce fresh and successful ideas to our that have not been recommended by major research firms and allows our readers to take advantage of opportunities early on.</p>
</section>
<div class="abs rule"></div>

<section class="abs col" style="left:60px;width:192px">
  <h2>ABOUT US</h2>
  <p class="lead">To access our TCLM ST Trades, Current Portfolio, Daily must subscribe to our FREE 2 Week Trail click here.</p>
  <p>Where have you been all my life! A friend of mine who subscribes The Calm Ledger Merchant talked me into a free trial subscription recently. I have been trading stock for well over 30 years and have have told all my friends about the service.</p>
  <p>Where have you been all my life! A friend of mine who subscribes to The Calm Ledger Merchant talked me into a free trial subscription and have &nbsp;have told all my friends about the service.</p>
  <span class="more">READ MORE</span>
</section>

<section class="abs col" style="left:275px;width:186px">
  <h2 style="display:flex;justify-content:space-between;align-items:center">MARKET NEWS <span style="color:#aaa;font-size:9px;font-family:Arimo,sans-serif">‹ &nbsp;›</span></h2>
  <div class="news-img" role="img" aria-label="Photo of a tablet showing a rising business graph with small figures"><span class="news-date">22 March 2015</span></div>
  <p style="margin-top:8px">Where have you been all my life! A friend of mine who subscribes to The Calm Ledger Merchant talked me into a free trial subscription have told all my friends about the service. <span style="color:var(--gold)">View All</span></p>
</section>

<section class="abs col" style="left:485px;width:181px">
  <h2>OUR SERVICES</h2>
  <p>Where have you been all my life! A friend of mine who subscribes to The Calm Ledger Merchant talked me into a free trial amount of winners as you have had in your reports.</p>
  <ul class="services">
    <li><i class="dot"></i>Daily Email Updates on Current &nbsp;Positions</li>
    <li><i class="dot"></i>Private Insider Feed for Traders</li>
    <li><i class="dot"></i>TCLM 15 Fab Index</li>
    <li><i class="dot"></i>Weekly Report on New Recommendations</li>
    <li><i class="dot"></i>Live Feed on Market News</li>
    <li><i class="dot"></i>Our Short Term Trades</li>
    <li><i class="dot"></i>Our Current Portfolio</li>
  </ul>
</section>

<section class="abs band"></section>
<div class="abs monitor" role="img" aria-label="Desktop monitor showing a portfolio performance line chart against major indices"></div>
<section class="abs band-text">
  <h2>TCLM TOP TEN RECOMMENDATIONS OF Q1 2015</h2>
  <p>The Alerts Portfolio had 67 recommendations for a total profit of $47,435. The 67 recommendations had 46 correct trades for a win ratio of 69%. The average return on each trade was 9.37% with an average holding period of 5.64 days.The 56 recommendaThe average return on each trade was 2.36% with an average holding period of 20.06 days I've been a subscriber since April 2014 and what a ride it's been!. I have in the past subscribed to a number of investment newsletters and advisory services which sometimes is hard to believe......Miles</p>
  <p>I have in the past subscribed to a number of investment newsletters and advisory services and blown a lot of money along the advisory services and blown a lot of money along the way, without any tangible results to show.</p>
</section>
<div class="abs subscribe"><span>Enter Your Email Id :</span><b>SUBSCRIBE NOW <svg width="8" height="8" viewBox="0 0 10 10"><circle cx="5" cy="5" r="4.2" stroke="#fff" fill="none" stroke-width="1.2"/><path d="M4 3l2 2-2 2" stroke="#fff" fill="none" stroke-width="1.2"/></svg></b></div>

<section class="abs report">
  <h2>LATEST REPORT</h2>
  <div class="sub">Our Team of Researchers, Stock Traders and Contributors would like to The Calm Ledger Merchant",</div>
  <p>The Alerts Portfolio had 67 recommendations for a total profit of $47,435. The 67 recommendations had 46 correct trades for a win ratio of 69%. The average return on each trade was 9.37% with an average holding period of 5.64 days.The 56 recommendaThe average return on each trade was 2.36% with an average holding period of 20.06 days I've been subscribed to a number of investment newsletters and advisory services which sometimes is hard to believe......Miles</p>
</section>
<div class="abs pager"><i></i><i class="on"></i><i></i></div>

<footer class="abs footer">
  <div class="abs fcol" style="left:61px;width:200px">
    <h3>STAY IN TOUCH!</h3>
    <p>Follow US in our social networks! Lorem ipsum dolor sit amet, conse It is a long established fact that a reader will be distracted by the a page ctetur and go adipiscing elit.</p>
    <div class="social"><i></i><i></i><i></i><i></i></div>
  </div>
  <div class="abs fcol" style="left:282px;width:180px">
    <h3>OUR LOCATION</h3>
    <ul class="contact">
      <li><svg width="6" height="8" viewBox="0 0 6 8"><path d="M3 8C1 5 0 4 0 3a3 3 0 0 1 6 0c0 1-1 2-3 5z" fill="var(--gold)"/><circle cx="3" cy="3" r="1" fill="var(--navy)"/></svg>Address : 2/3 calm Ledger Merchant<br>lorem ipsum dummy</li>
      <li><svg width="7" height="7" viewBox="0 0 10 10"><path d="M2 0l2 2.5-1.2 1.3a6 6 0 0 0 3.4 3.4L7.5 6 10 8 8.5 10C4 10 0 6 0 1.5z" fill="var(--gold)"/></svg>Phone : 877-555-0142</li>
      <li><svg width="8" height="6" viewBox="0 0 8 6"><rect width="8" height="6" fill="var(--gold)"/><path d="M0 0l4 3 4-3" stroke="var(--navy)" fill="none" stroke-width=".8"/></svg>Email : info@thecalmledgermerchant.com</li>
    </ul>
  </div>
  <div class="abs fcol" style="left:486px;width:182px">
    <h3>NEWSLETTER</h3>
    <p>Lorem ipsum dolor sit amet, consectetur adi sollicitud ante tellus ornare mi, et mollis</p>
    <div class="news-form"><span>Enter Your Email Id :</span><b>SUBSCRIBE</b></div>
  </div>
</footer>
<div class="abs copy">© Copy Right 2105 Calm Ledger Merchant .All copyrights Reserved.</div>

</body>
</html>
```